Design flyer for CWFM

Cedar Well Fellowship Ministry (CWFM)
• The praise and worship team of RTGC
• The vision is to support members become the praise of God
• The mandate is to help members actualize the glorious privilege to be His praise
• Organize and coordinate Bright Dawn Chorus Gathering and Rivers of Stillness
• Goal is to enable members learn to worship God in spirit and in truth
• CWFM is made up of chapter praise team BLOVF praise team, the international Unity Singers and the Psalmody School
• The goal is to manifest God’s glory as we worship Him in spirit and in truth

Join Cedar Well Fellowship Ministry

```html
<!DOCTYPE html>
<html lang="en">
<head>
<meta charset="utf-8">
<title>Cedar Well Fellowship Ministry</title>
<link rel="stylesheet" href="https://fonts.googleapis.com/css2?family=Courgette&family=Noto+Sans:wght@700&display=swap">
<style>
  :root {
    --ink-blue: #1d5ad8;
    --sky-top: #2a78d6;
    --sky-mid: #8ec3ef;
    --sky-glow: #eaf6ff;
    --grass-light: #7fd13a;
    --grass-dark: #3f9a1e;
    --paper: #ffffff;
    --wave-line: #9fb6e8;
    --wave-deep: #2f7fd6;
    --wave-light: #8fd0f2;
    --logo-ring: #2d5fa8;
  }
  html, body {
    margin: 0;
    padding: 0;
    overflow: hidden;
    background: var(--paper);
  }
  .flyer {
    position: relative;
    width: 929px;
    height: 1200px;
    overflow: hidden;
    background: var(--paper);
    font-family: "Noto Sans", Verdana, sans-serif;
    font-weight: 700;
    color: var(--ink-blue);
  }
  .hero {
    position: absolute;
    left: 0;
    top: 0;
    width: 929px;
    height: 420px;
    background:
      radial-gradient(ellipse 180px 140px at 470px 160px, var(--sky-glow) 0%, rgba(234,246,255,0) 100%),
      linear-gradient(180deg, var(--sky-top) 0%, var(--sky-mid) 45%, #d8ecfa 64%, var(--grass-light) 66%, var(--grass-dark) 100%);
  }
  .hero-title {
    position: absolute;
    left: 0;
    top: 10px;
    width: 929px;
    margin: 0;
    text-align: center;
    font-family: "Courgette", cursive;
    font-weight: 400;
    font-size: 58px;
    color: var(--paper);
    letter-spacing: 1px;
  }
  .hero-swoosh {
    position: absolute;
    left: 0;
    top: 300px;
    width: 929px;
    height: 150px;
  }
  .footer-wave {
    position: absolute;
    left: 0;
    bottom: 0;
    width: 929px;
    height: 160px;
  }
  .brand {
    position: absolute;
    left: 25px;
    top: 432px;
    display: flex;
    align-items: center;
    gap: 16px;
  }
  .brand-mark {
    width: 114px;
    height: 114px;
    border-radius: 50%;
    border: 6px solid var(--logo-ring);
    box-sizing: border-box;
  }
  .brand-name {
    font-size: 22px;
    line-height: 1.2;
    color: var(--logo-ring);
    max-width: 260px;
  }
  .columns {
    position: absolute;
    left: 18px;
    top: 564px;
    width: 900px;
    display: flex;
    gap: 14px;
  }
  .col-left { width: 410px; }
  .col-right { width: 476px; }
  .ministry-title {
    margin: 0 0 22px;
    font-size: 29px;
    line-height: 1.3;
  }
  .points {
    list-style: none;
    margin: 0;
    padding: 0;
    font-size: 21px;
    line-height: 32px;
  }
  .points li::before { content: "\2022\00a0"; }
  .col-right .points li { margin-bottom: 32px; }
  .join {
    margin: 0;
    font-size: 29px;
    line-height: 1.2;
  }
</style>
</head>
<body>
<main class="flyer">
  <div class="hero" role="img" aria-label="Bright sky with sun and clouds over a green meadow with a single tree"></div>
  <h1 class="hero-title">Radiant Tide</h1>
  <svg class="hero-swoosh" viewBox="0 0 929 150" preserveAspectRatio="none" aria-hidden="true">
    <path d="M0 95 C 150 60, 280 20, 380 40 C 480 60, 560 150, 700 140 C 800 132, 870 110, 929 90 L929 150 L0 150 Z" fill="var(--paper)"/>
    <path d="M0 100 C 160 70, 300 50, 420 70 C 540 90, 620 135, 760 120" fill="none" stroke="var(--wave-line)" stroke-width="1.5"/>
    <path d="M200 60 C 320 30, 430 40, 520 90" fill="none" stroke="#6fae4a" stroke-width="1"/>
  </svg>

  <div class="brand">
    <span class="brand-mark"></span>
    <span class="brand-name">Radiant Tide Global Communion</span>
  </div>

  <section class="columns">
    <div class="col-left">
      <h2 class="ministry-title">Cedar Well Fellowship Ministry (CWFM)</h2>
      <ul class="points">
        <li>The praise and worship team of RTGC</li>
        <li>The vision is to support members become the praise of God</li>
        <li>The mandate is to help members actualize the glorious privilege to be His praise</li>
        <li>Organize and coordinate Bright Dawn Chorus Gathering and Rivers of Stillness</li>
      </ul>
    </div>
    <div class="col-right">
      <ul class="points">
        <li>Organize and coordinate Bright Dawn Chorus Gathering and Rivers of Stillness</li>
        <li>Goal is to enable members learn to worship God in spirit and in truth</li>
        <li>CWFM is made up of chapter praise team BLOVF praise team, the international Unity Singers and the Psalmody School</li>
        <li>The goal is to manifest God’s glory as we worship Him in spirit and in truth</li>
      </ul>
      <p class="join">Join Cedar Well Fellowship Ministry</p>
    </div>
  </section>

  <svg class="footer-wave" viewBox="0 0 929 160" preserveAspectRatio="none" aria-hidden="true">
    <defs>
      <linearGradient id="footerFill" x1="0" y1="0" x2="0" y2="1">
        <stop offset="0" stop-color="var(--wave-light)"/>
        <stop offset="1" stop-color="var(--wave-deep)"/>
      </linearGradient>
    </defs>
    <path d="M0 70 C 200 20, 420 40, 600 90 C 740 125, 860 110, 929 95 L929 160 L0 160 Z" fill="url(#footerFill)"/>
    <path d="M0 60 C 220 10, 430 30, 620 80 C 760 115, 870 100, 929 85" fill="none" stroke="var(--wave-line)" stroke-width="1.5"/>
    <path d="M0 90 C 240 40, 450 70, 640 110 C 780 135, 880 125, 929 115" fill="none" stroke="var(--paper)" stroke-width="1.5"/>
  </svg>
</main>
</body>
</html>
```